Styling of small website for mid-sized Engineering and Manufacturing company

We need the styling for a professional website for a company wich delivers: engineering, manufacturing, assembling, servicing and prototyping. (typically, they produce complex devices in limited series (1-100 pieces. The client comes with an idea and they translate it into design and device).
We have already made a wire-frame, but need a style (colors, fonts, H1, H2, paragraphs, margins, padding etc).
The style must :
- express profession attitude (world of engineering)
- have a fresh, modern look
- be sober (enough (white) space between the elements
The style must also be able to be used in a RWD. At this moment the logo (just letters) uses a green color (#4C6E33), but it isn't an obligation to use the exact same color (even not the 'green' color itself if you think another color is better for the site).
engineering and production
It Company
Coded - Design and coding required
5+ page

```html
<!DOCTYPE html>
<html lang="en">
<head>
<meta charset="utf-8">
<title>Norvane Holding</title>
<link href="https://fonts.googleapis.com/css2?family=Open+Sans:wght@400;600;700;800&display=swap" rel="stylesheet">
<style>
:root{
  --orange:#f47a1f;
  --text:#555;
  --heading:#333;
  --red:#b3262e;
  --tile-orange:#df6a13;
  --green:#1f8a3f;
  --blue:#2f6db4;
  --footer:#3a3a3a;
  --footer-bottom:#2f2f2f;
  --footer-text:#9a9a9a;
  --panel:#f0f0f0;
  --tick:#6cb33f;
}
*{margin:0;padding:0;box-sizing:border-box}
html,body{width:865px;height:1200px;overflow:hidden;background:#fff}
body{position:relative;font-family:'Open Sans',Arial,sans-serif;color:var(--text)}
.abs{position:absolute}
.header{top:0;left:0;width:865px;height:56px;background:#fff}
.brand{left:71px;top:17px;display:flex;align-items:center;gap:7px}
.brand-mark{width:22px;height:22px;border-radius:50%;background:var(--orange)}
.brand-name{font-size:18px;font-weight:700;color:#555;letter-spacing:-.3px}
.nav{top:0;left:0;width:865px;height:56px}
.nav a{position:absolute;top:24px;font-size:10.4px;color:#555;text-decoration:none;transform:translateX(-50%);white-space:nowrap}
.hero{top:56px;left:0;width:865px;height:323px;background:linear-gradient(100deg,#3b4148 0%,#5a6168 35%,#4a5057 60%,#2c3238 100%)}
.hero-figure{top:56px;left:490px;width:340px;height:323px;background:linear-gradient(180deg,#3a4556 0%,#2a3444 60%,#6b4a3a 100%);opacity:.55}
.hero-title{top:155px;left:71px;font-size:30px;font-weight:700;color:var(--orange);letter-spacing:.3px}
.hero-sub{top:197px;left:71px;font-size:16px;line-height:25px;font-weight:700;color:#fff;letter-spacing:.2px}
.hero-btn{top:256px;left:72px;width:100px;height:32px;background:var(--orange);color:#fff;font-size:10.5px;font-weight:700;display:flex;align-items:center;justify-content:center;border-radius:2px}
.h2{font-size:14.5px;font-weight:700;color:var(--heading);text-transform:uppercase}
.intro-title{top:421px;left:71px}
.para{left:71px;width:723px;font-size:9.2px;line-height:18.4px;color:var(--text)}
.intro-text{top:451px}
.services{top:535px;left:71px;width:724px;height:130px;display:flex}
.service{width:181px;height:130px;position:relative;border-right:1px solid #fff}
.service:last-child{border-right:0}
.service-img{height:102px}
.service-label{height:28px;color:#fff;font-size:10.5px;font-weight:700;padding-left:13px;display:flex;align-items:center}
.shadow{top:665px;left:100px;width:665px;height:18px;background:radial-gradient(ellipse at top,rgba(0,0,0,.28),rgba(0,0,0,0) 70%)}
.second-text{top:704px}
.showcase-title{top:797px;left:71px;font-size:12px}
.why-title{top:797px;left:553px;font-size:12px}
.showcase-img{top:833px;left:71px;width:174px;height:116px;background:linear-gradient(180deg,#4fa2dc 0%,#8cc6ee 45%,#5a9a3a 70%,#f2c21b 100%)}
.showcase-text{top:831px;left:269px;width:256px;font-size:8.4px;line-height:16.8px}
.why-box{top:833px;left:553px;width:241px;height:116px;background:var(--panel);border:1px solid #ddd;padding:17px 0 0 18px}
.why-box li{list-style:none;display:flex;align-items:center;gap:8px;font-size:10.4px;color:#444;height:28.5px}
.footer{top:998px;left:0;width:865px;height:170px;background:var(--footer)}
.footer-bottom{top:1168px;left:0;width:865px;height:32px;background:var(--footer-bottom);color:#8a8a8a;font-size:7.8px;display:flex;align-items:center;justify-content:center}
.fcol{top:1025px}
.fcol h3{font-size:9.6px;font-weight:700;color:#fff;margin-bottom:8px}
.fcol p,.fcol a{display:block;font-size:8px;line-height:16.8px;color:var(--footer-text);text-decoration:none}
.fcol .map{color:#bbb;font-weight:700;font-size:7.6px}
.contact-line{display:flex;align-items:center;gap:7px;margin-bottom:4px}
.social{display:flex;align-items:center;gap:4px;margin-bottom:11px;font-size:8px;color:var(--footer-text)}
.social span.dot{width:20px;height:20px;border-radius:50%;background:#555}
</style>
</head>
<body>
<header class="abs header">
  <div class="abs brand"><span class="brand-mark"></span><span class="brand-name">Norvaneholding</span></div>
  <nav class="abs nav">
    <a href="#" style="left:367px">Home</a>
    <a href="#" style="left:444px">Services</a>
    <a href="#" style="left:526px">Portfolio</a>
    <a href="#" style="left:602px">News</a>
    <a href="#" style="left:686px">About NORVANE</a>
    <a href="#" style="left:776px">Contact</a>
  </nav>
</header>

<section class="abs hero" role="img" aria-label="Engineer in hard hat and high-visibility jacket in front of heavy industrial machinery"></section>
<div class="abs hero-figure" role="img" aria-label="Worker in orange safety helmet"></div>
<h1 class="abs hero-title">NORVANE HOLDING</h1>
<p class="abs hero-sub">ENGINEERING, MANUFACTURING, ASSEMBLING,<br>SERVICING AND PROTOTYPING.</p>
<a class="abs hero-btn">CLICK HERE</a>

<h2 class="abs h2 intro-title">Technological solutions from idea to product</h2>
<p class="abs para intro-text">Lorem Ipsum is simply dummy text of the printing and typesetting industry. Lorem Ipsum has been the industry's standard dummy text ever since the 1500s, when an unknown printer took a galley of type and scrambled it to make a type specimen book. It has survived not only five centuries, but also the leap into electronic typesetting, remaining essentially unchanged. It was popularised in the 1960s with the release of Letraset sheets containing...</p>

<div class="abs services">
  <div class="service">
    <div class="service-img" role="img" aria-label="Businessman standing before a wall of golden gears" style="background:linear-gradient(160deg,#c9a66a,#8a6a3c 60%,#d8d2c4)"></div>
    <div class="service-label" style="background:var(--red)">ENGINEERING</div>
  </div>
  <div class="service">
    <div class="service-img" role="img" aria-label="Metal bearings and parts on technical drawings" style="background:linear-gradient(160deg,#e4e8ee,#a9b1bc 55%,#5c636d)"></div>
    <div class="service-label" style="background:var(--tile-orange)">PROTOTYPING</div>
  </div>
  <div class="service">
    <div class="service-img" role="img" aria-label="Close-up of polished steel and copper machine flanges" style="background:linear-gradient(160deg,#6e7379,#b58460 50%,#3a3e44)"></div>
    <div class="service-label" style="background:var(--green)">ASSEMBLEREN</div>
  </div>
  <div class="service">
    <div class="service-img" role="img" aria-label="Two engineers in orange helmets inspecting a factory installation" style="background:linear-gradient(160deg,#c8b48a,#8ea0b8 50%,#2f3a4a)"></div>
    <div class="service-label" style="background:var(--blue)">SERVICING</div>
  </div>
</div>
<div class="abs shadow"></div>

<p class="abs para second-text">Lorem Ipsum is simply dummy text of the printing and typesetting industry. Lorem Ipsum has been the industry's standard dummy text ever since the 1500s, when an unknown printer took a galley of type and scrambled it to make a type specimen book. It has survived not only five centuries, but also the leap into electronic typesetting, remaining essentially unchanged. It was popularised in the 1960s with the release of Letraset sheets containing...</p>

<h2 class="abs h2 showcase-title">Showcase client</h2>
<div class="abs showcase-img" role="img" aria-label="Crane and city buildings on a yellow hard hat against blue sky"></div>
<p class="abs showcase-text">Lorem Ipsum is simply dummy text of the printing and typesetting industry. Lorem Ipsum has been the industry's standard dummy text ever since the 1500s, when an unknown printer took a galley of type and scrambled it to make a type specimen book. It has survived not only five centuries, but also the leap into electronic typesetting, remaining essentially unchanged. It was popularised in the 1960s with the release of Letraset sheets containing...</p>

<h2 class="abs h2 why-title">Waarom klanten voor ons kiezen</h2>
<ul class="abs why-box">
  <li><svg width="12" height="10" viewBox="0 0 12 10"><path d="M1 5.5 4.3 8.5 11 1.5" fill="none" stroke="var(--tick)" stroke-width="2.2"/></svg>Al 4.251 abonners</li>
  <li><svg width="12" height="10" viewBox="0 0 12 10"><path d="M1 5.5 4.3 8.5 11 1.5" fill="none" stroke="var(--tick)" stroke-width="2.2"/></svg>1 keer per maand</li>
  <li><svg width="12" height="10" viewBox="0 0 12 10"><path d="M1 5.5 4.3 8.5 11 1.5" fill="none" stroke="var(--tick)" stroke-width="2.2"/></svg>Exclusive tips en promo's</li>
</ul>

<footer class="abs footer"></footer>
<div class="abs fcol" style="left:71px">
  <h3>WELCOME</h3>
  <a href="#">Home</a><a href="#">Services</a><a href="#">Portfolio</a><a href="#">News</a><a href="#">About NORVANE</a><a href="#">Contact</a>
</div>
<div class="abs fcol" style="left:198px">
  <h3>CONTACT US</h3>
  <p class="contact-line"><svg width="9" height="7" viewBox="0 0 9 7"><rect width="9" height="7" fill="#888"/><path d="M0 0 4.5 4 9 0" fill="none" stroke="#3a3a3a"/></svg>info@norvane.example</p>
  <p class="contact-line"><svg width="9" height="9" viewBox="0 0 9 9"><path d="M2 0 3.5 2.5 2.5 3.5Q3.5 5.5 5.5 6.5L6.5 5.5 9 7 8 9Q2 8.5 0 1Z" fill="#888"/></svg>+32 100 00 00</p>
</div>
<div class="abs fcol" style="left:338px">
  <h3>OUR SALES DEPARTMENT</h3>
  <p>120 Street name, State name,<br>Country name, zip code : 3265523</p>
  <a class="map" href="#">VIEW MAP</a>
</div>
<div class="abs fcol" style="left:523px">
  <h3>R&amp;D AND PRODUCTION</h3>
  <p>120 Street name, State name,<br>Country name, zip code : 3265523</p>
  <a class="map" href="#">VIEW MAP</a>
</div>
<div class="abs fcol" style="left:719px">
  <h3>FOLLOW US</h3>
  <div class="social"><span class="dot"></span>: Community</div>
  <div class="social"><span class="dot"></span>: Updates</div>
  <div class="social"><span class="dot"></span>: Network</div>
</div>
<div class="abs footer-bottom">Copyrights © 2015. Norvane holding. All Rights Reserved.</div>
</body>
</html>
```